Trailer wrap

Looking for a trailer wrap. I have attached a file of my logo. Also use the phone number 555-304-2617. integrate one or both of the following slogans - ""Solutions You Can Trust" - ""Prompt. Able. Careful. Honest. That’s the PACH Difference" If possible integrate a United States flag, possibly in grayscale. The following are my colors: Orange F16A21 Blue 4D91D9.

```html
<!DOCTYPE html>
<html lang="en">
<head>
<meta charset="utf-8">
<title>PACH HVAC &amp; Plumbing – Trailer Wrap</title>
<link rel="stylesheet" href="https://fonts.googleapis.com/css2?family=Anton&family=Poppins:ital,wght@0,600;1,700&display=swap">
<style>
  :root {
    --orange: #F16A21;
    --orange-deep: #E2401F;
    --blue: #4D91D9;
    --navy: #1C4F8F;
    --white: #FFFFFF;
    --page: #FFFFFF;
  }
  * { margin: 0; padding: 0; box-sizing: border-box; }
  html, body { width: 1200px; height: 1001px; overflow: hidden; background: var(--page); }
  .canvas { position: relative; width: 1200px; height: 1001px; }

  .wrap-panel {
    position: absolute;
    left: 40px; top: 255px;
    width: 1120px; height: 490px;
    overflow: hidden;
    box-shadow: 0 0 0 1px #d6d9de;
  }
  .wrap-art { position: absolute; inset: 0; width: 100%; height: 100%; }

  .brand {
    position: absolute;
    left: 208px; top: 128px; width: 360px;
    font-family: "Poppins", sans-serif;
    font-weight: 600;
    font-size: 23px;
    letter-spacing: 1px;
    white-space: nowrap;
    color: var(--orange);
    display: flex; align-items: center; justify-content: center; gap: 10px;
  }
  .brand-dot { width: 16px; height: 16px; border-radius: 50%; background: var(--blue); flex: none; }

  .phone {
    position: absolute;
    left: 222px; top: 244px;
    display: flex; align-items: center; gap: 10px;
  }
  .phone-icon { width: 22px; height: 22px; flex: none; }
  .phone-number {
    font-family: "Anton", sans-serif;
    font-size: 50px; line-height: 1;
    color: var(--blue);
    -webkit-text-stroke: 2px var(--navy);
    transform: skewX(-10deg);
    letter-spacing: -1px;
    white-space: nowrap;
  }

  .headline {
    position: absolute;
    left: 662px; top: 148px; width: 340px;
    text-align: center;
    font-family: "Anton", sans-serif;
    font-weight: 400;
    line-height: 1;
    transform: skewX(-10deg);
  }
  .headline-top {
    display: block; font-size: 50px;
    color: var(--orange);
    -webkit-text-stroke: 2px #8a2a0c;
  }
  .headline-bottom {
    display: block; font-size: 52px; margin-top: 4px;
    color: var(--blue);
    -webkit-text-stroke: 2px var(--navy);
  }

  .rule {
    position: absolute;
    left: 640px; top: 278px; width: 384px; height: 3px;
    background: var(--orange);
  }
  .tagline {
    position: absolute;
    left: 632px; top: 290px; width: 400px;
    font-family: "Poppins", sans-serif;
    font-style: italic; font-weight: 700;
    font-size: 20px; line-height: 28px;
    color: var(--white);
    text-align: center;
    white-space: nowrap;
  }
  .tagline .accent { color: var(--orange); }
</style>
</head>
<body>
<main class="canvas">
  <section class="wrap-panel">
    <svg class="wrap-art" viewBox="0 0 1120 490" preserveAspectRatio="none">
      <defs>
        <linearGradient id="blueField" x1="0" y1="0" x2="0" y2="1">
          <stop offset="0" stop-color="#4D91D9"/>
          <stop offset="0.65" stop-color="#3F80CB"/>
          <stop offset="1" stop-color="#1C4F8F"/>
        </linearGradient>
        <linearGradient id="orangeField" x1="0" y1="0" x2="1" y2="0">
          <stop offset="0" stop-color="#E2401F"/>
          <stop offset="0.45" stop-color="#F16A21"/>
          <stop offset="1" stop-color="#F16A21"/>
        </linearGradient>
        <linearGradient id="flagTone" x1="0" y1="0" x2="1" y2="0.4">
          <stop offset="0" stop-color="#FFFFFF"/>
          <stop offset="0.3" stop-color="#BDBDBD"/>
          <stop offset="1" stop-color="#6B6B6B"/>
        </linearGradient>
      </defs>

      <rect class="base" width="1120" height="490" fill="#FFFFFF"/>

      <path class="flag-area" role="img" aria-label="Waving United States flag in grayscale"
            d="M700 0 H1120 V262 C1040 235 930 215 800 225 C740 230 690 245 640 262 C730 190 790 90 700 0 Z"
            fill="url(#flagTone)"/>

      <path class="blue-field"
            d="M115 490 C300 440 450 380 560 310 C640 260 700 235 800 225 C930 215 1040 235 1120 262 V490 Z"
            fill="url(#blueField)"/>

      <path class="orange-field"
            d="M0 0 H170 C95 130 120 300 300 360 C400 392 500 370 590 300 C480 400 330 460 95 490 H0 Z"
            fill="url(#orangeField)"/>

      <rect class="front-face" x="0" y="0" width="112" height="490" fill="#D8401B" opacity="0.5"/>

      <path class="navy-arc"
            d="M178 0 C100 130 130 318 320 364 C430 390 530 352 612 283 C520 342 420 364 320 346 C162 302 142 130 206 0 Z"
            fill="#1C4F8F"/>

      <path class="swoosh-navy" d="M780 0 L790 0 C740 100 680 160 590 205 C665 150 730 95 780 0 Z" fill="#1C4F8F"/>
      <path class="swoosh-blue" d="M800 0 L820 0 C765 110 700 170 605 218 C685 160 748 100 800 0 Z" fill="#4D91D9"/>
      <path class="swoosh-orange" d="M850 0 L874 0 C805 120 705 212 560 264 C680 200 772 118 850 0 Z" fill="#F16A21"/>
    </svg>

    <div class="brand"><span class="brand-dot"></span>PACH HVAC &amp; Plumbing</div>

    <div class="phone">
      <svg class="phone-icon" viewBox="0 0 24 24" aria-hidden="true">
        <circle cx="12" cy="12" r="10.5" fill="none" stroke="#4D91D9" stroke-width="2"/>
        <path d="M8.6 7.2c.4-.4 1-.4 1.3 0l1 1.3c.3.4.3.9-.1 1.2l-.6.6c.5 1.2 1.4 2.1 2.6 2.6l.6-.6c.3-.4.8-.4 1.2-.1l1.3 1c.4.3.4.9 0 1.3l-.7.7c-.6.6-1.6.7-2.4.3-2.1-1-3.8-2.7-4.8-4.8-.4-.8-.3-1.8.3-2.4z" fill="#4D91D9"/>
      </svg>
      <span class="phone-number">555-304-2617</span>
    </div>

    <h1 class="headline">
      <span class="headline-top">SOLUTIONS</span>
      <span class="headline-bottom">YOU CAN TRUST</span>
    </h1>

    <div class="rule"></div>
    <p class="tagline">Prompt. Able. Careful. Honest.<br>That’s the <span class="accent">PACH</span> Difference</p>
  </section>
</main>
</body>
</html>
```